Cat sitting business Web Design Project ***

I have a cat sitting business where I either take care of cats in their home or board them in mine

I need a website which offers my services, my rates, about me, FAQ's, Hours of operation and service areas covered, testimonials, contact info, newsletter sign up, gallery of photos and the ability for me to go in and update when needed.

Coding

Coded - Design and coding required

Number of Pages Required

5+ page

```html
<!DOCTYPE html>
<html lang="en">
<head>
<meta charset="utf-8">
<title>Velvet Paws Cat Sitting</title>
<link rel="stylesheet" href="https://fonts.googleapis.com/css2?family=Fredoka:wght@500;600&family=Poppins:wght@400;500;600&family=Mrs+Saint+Delafield&display=swap">
<style>
:root{
  --rose:#b06063;
  --rose-dark:#9a4f52;
  --green:#8dc64a;
  --green-soft:#96c94a;
  --ink:#2f2f2f;
  --grey:#777;
  --line:#e6e6e6;
  --stage:#e8e9eb;
  --white:#fff;
}
*{box-sizing:border-box;margin:0;padding:0}
html,body{width:712px;height:1200px;overflow:hidden;background:var(--stage)}
body{position:relative;font-family:"Poppins",sans-serif;color:var(--ink)}
.page{position:absolute;left:183px;top:0;width:630px;height:2190px;background:var(--white);transform:scale(.5479);transform-origin:0 0;overflow:hidden}
.abs{position:absolute}
.display{font-family:"Fredoka",sans-serif;font-weight:600}
.script{font-family:"Mrs Saint Delafield",cursive;color:var(--rose);font-size:22px;line-height:1}
.body-text{font-size:7px;line-height:9.5px;color:var(--grey)}
.btn{position:absolute;height:16px;border-radius:8px;font-size:5.5px;font-weight:600;display:flex;align-items:center;justify-content:center}
.btn-green{background:var(--green);color:var(--white)}
.btn-outline{border:1px solid var(--rose);color:var(--rose);background:var(--white)}
.hl{background:var(--green);color:var(--white);padding:0 3px}

/* top bar */
.topbar{left:0;top:0;width:630px;height:17px;background:var(--rose);color:var(--white);font-size:5px;display:flex;align-items:center;gap:18px;padding-left:65px}
.topbar .social{position:absolute;right:45px;top:5px;display:flex;gap:3px}
.dot{width:7px;height:7px;border-radius:50%;border:1px solid var(--white)}

/* header */
.logo{left:55px;top:26px;width:70px;text-align:center}
.logo .mark{width:26px;height:26px;border-radius:50%;border:1.5px solid var(--green);margin:0 auto 3px}
.logo .name{font-size:7px;font-weight:500;color:var(--rose);line-height:8px}
.nav{left:300px;top:37px;display:flex;align-items:center;gap:20px;font-size:5.5px;font-weight:600;color:var(--white)}
.nav .cta{background:var(--rose);padding:5px 9px;border-radius:9px}

/* hero */
.hero-title{left:65px;top:116px;font-size:26px;line-height:32px;color:var(--rose)}
.hero-title .g{color:var(--green)}
.hero-photo{left:323px;top:73px}

/* services */
.svc{width:110px;text-align:center}
.svc .circle{width:52px;height:52px;border-radius:50%;margin:0 auto;position:relative;border:3px solid #f1dede}
.svc .circle.g{border-color:#e3f0d2}
.svc .badge{position:absolute;right:-8px;top:-10px;width:13px;height:13px;border-radius:50%;color:var(--white);font-size:6px;display:flex;align-items:center;justify-content:center;border:2px solid var(--white)}
.svc h3{font-size:9.5px;font-weight:600;margin:8px 0 4px}
.bg-rose{background:var(--rose)}
.bg-green{background:var(--green)}
.help-title{right:43px;top:402px;text-align:right;font-size:17px;line-height:22px;color:var(--ink);font-weight:600;font-family:"Poppins",sans-serif}
.ticks{right:43px;top:500px;font-size:5.3px;font-weight:600;text-align:right}
.ticks li{list-style:none;height:16px;display:flex;align-items:center;justify-content:flex-end;gap:4px}
.tick{width:9px;height:9px;border-radius:50%;background:var(--rose);display:inline-flex;align-items:center;justify-content:center}

/* about */
.about-photo{left:325px;top:675px;width:305px;height:272px;background:linear-gradient(135deg,#e7c98d 0%,#d9b47a 40%,#3a3432 60%,#ece9e6 85%)}
.h2{font-size:16px;font-weight:600;font-family:"Poppins",sans-serif;color:var(--ink)}

/* testimonial */
.quote-mark{font-family:"Fredoka",sans-serif;color:var(--white);font-size:60px;line-height:1;opacity:.9}
.arrow{width:14px;height:14px;border-radius:50%;background:var(--rose);border:2px solid var(--white)}

/* faq */
.acc{left:380px;width:207px;background:#fafafa;border:1px solid #f0f0f0;font-size:6.5px;font-weight:600;color:var(--rose)}
.acc .q{height:22px;display:flex;align-items:center;justify-content:space-between;padding:0 10px}

/* pricing */
.card{width:135px;height:274px;background:var(--white);box-shadow:0 2px 6px rgba(0,0,0,.12)}
.card .photo{height:74px}
.card .top{display:flex;align-items:center;gap:8px;padding:9px 12px 0}
.price{background:var(--green);color:var(--white);font-size:8px;font-weight:600;padding:1px 5px}
.card .plan{font-size:9.5px;font-weight:600}
.card .per{font-family:"Mrs Saint Delafield",cursive;color:var(--rose);font-size:9px;padding-left:14px}
.card p{font-size:6.5px;line-height:9px;color:var(--grey);text-align:center;padding:14px 12px 10px}
.card li{list-style:none;font-size:6.5px;font-weight:600;display:flex;align-items:center;gap:8px;padding:0 0 0 20px;height:25px}
.card .tick{background:var(--green);width:11px;height:11px}
.partner{width:50px;height:10px;border-radius:5px;background:#d4d4d4}

/* footer */
.field{height:22px;border:1px solid var(--white);border-radius:11px;color:var(--white);font-size:6px;font-weight:600;display:flex;align-items:center;padding-left:10px}
.foot h4{font-size:7px;font-weight:600;color:var(--white);margin-bottom:8px}
.foot li{list-style:none;font-size:5px;font-weight:600;color:var(--white);height:13px;display:flex;align-items:center;gap:5px}
.copyright{left:0;top:2180px;width:630px;height:10px;background:var(--green);color:var(--white);font-size:6px;font-weight:600;text-align:center;line-height:10px}
</style>
</head>
<body>
<div class="page">

  <!-- hero shape -->
  <svg class="abs" style="left:0;top:0" width="630" height="460" viewBox="0 0 630 460">
    <path d="M160 17H630V350C595 330 530 345 470 332C420 318 405 265 375 205C345 145 255 135 205 85C182 62 166 40 160 17Z" fill="var(--green-soft)"/>
  </svg>
  <svg class="abs hero-photo" width="312" height="252" viewBox="0 0 312 252" role="img" aria-label="Photo of a tabby kitten being stroked under the chin">
    <defs>
      <radialGradient id="catTone" cx="45%" cy="50%" r="60%">
        <stop offset="0" stop-color="#b8ada2"/>
        <stop offset=".6" stop-color="#d9c3b1"/>
        <stop offset="1" stop-color="#efe7df"/>
      </radialGradient>
    </defs>
    <ellipse cx="156" cy="126" rx="154" ry="124" fill="url(#catTone)"/>
  </svg>

  <div class="abs topbar">
    <span>☎ 123-456-789</span><span>✉ info@youremail.com</span><span>◷ Your Email Here</span>
    <div class="social"><i class="dot"></i><i class="dot"></i><i class="dot"></i><i class="dot"></i><i class="dot"></i><i class="dot"></i></div>
  </div>

  <div class="abs logo"><div class="mark"></div><div class="name">Velvet Paws<br>Cat Sitting</div></div>
  <nav class="abs nav"><span>Home</span><span>About</span><span>Services</span><span>Pricings</span><span>FAQs</span><span>Blogs</span><span class="cta">Contact Me</span></nav>

  <h1 class="abs display hero-title">Devoted to Proper<br><span class="g">Cat Sitting</span><br>Services</h1>
  <span class="btn btn-green" style="left:65px;top:228px;width:62px">View Services</span>
  <span class="btn btn-outline" style="left:137px;top:228px;width:55px">Contact Me</span>

  <!-- services -->
  <div class="abs svc" style="left:72px;top:366px"><div class="circle bg-rose"><span class="badge bg-rose">1</span></div><h3>Cat Sitting</h3><p class="body-text">Lorem Ipsum is simply dummy text of the printing and typesetting industry.</p></div>
  <div class="abs svc" style="left:213px;top:366px"><div class="circle g bg-green"><span class="badge bg-green">2</span></div><h3>Cat Training</h3><p class="body-text">Lorem Ipsum is simply dummy text of the printing and typesetting industry.</p></div>
  <div class="abs svc" style="left:72px;top:492px"><div class="circle g bg-green"><span class="badge bg-green">3</span></div><h3>Full Diagnostics</h3><p class="body-text">Lorem Ipsum is simply dummy text of the printing and typesetting industry.</p></div>
  <div class="abs svc" style="left:213px;top:492px"><div class="circle bg-rose"><span class="badge bg-rose">4</span></div><h3>Cat Breeding</h3><p class="body-text">Lorem Ipsum is simply dummy text of the printing and typesetting industry.</p></div>

  <div class="abs script" style="right:45px;top:368px">What we do?</div>
  <h2 class="abs help-title">How we help you<br>professionaly?</h2>
  <p class="abs body-text" style="left:395px;top:463px;width:192px;text-align:right">Lorem Ipsum is simply dummy text of the printing and typesetting industry. Lorem Ipsum has been the industry's standard dummy text ever</p>
  <ul class="abs ticks">
    <li>That as guard as fresh lady careful a they he I sitting. <span class="tick"></span></li>
    <li>That as guard as fresh lady careful a they he I sitting. <span class="tick"></span></li>
    <li>That as guard as fresh lady careful a they he I sitting. <span class="tick"></span></li>
  </ul>
  <span class="btn btn-green" style="left:522px;top:555px;width:62px">Discover More</span>

  <!-- about -->
  <div class="abs about-photo" role="img" aria-label="Photo of the owner holding a white cat on a yellow sofa"></div>
  <div class="abs script" style="left:65px;top:712px">About us</div>
  <div class="abs" style="left:65px;top:737px;width:80px;height:1px;background:var(--rose)"></div>
  <h2 class="abs h2" style="left:64px;top:745px">How did we get <span class="hl">here?</span></h2>
  <p class="abs body-text" style="left:65px;top:780px;width:225px">Lorem Ipsum is simply dummy text of the printing and typesetting industry. Lorem Ipsum has been the industry's standard dummy text ever since the 1500s, when an unknown printer took a galley of type and scrambled it to make a type specimen book. It has survived not only five centuries, but also the leap into electronic typesetting, remaining essentially unchanged. It was popularised in the 1960s with the release of Letraset sheets con-</p>
  <span class="btn btn-green" style="left:65px;top:873px;width:62px">Contact Me</span>

  <!-- testimonial -->
  <svg class="abs" style="left:0;top:947px" width="630" height="162" viewBox="0 0 630 162">
    <path d="M0 0H630V158C600 160 570 130 530 132C490 134 470 160 420 158C370 156 360 132 310 130C260 128 240 158 190 156C140 154 120 130 80 132C40 134 20 150 0 148Z" fill="var(--green)"/>
  </svg>
  <div class="abs quote-mark" style="left:130px;top:960px">“</div>
  <div class="abs quote-mark" style="left:460px;top:1025px">”</div>
  <h2 class="abs display" style="left:0;top:960px;width:630px;text-align:center;font-size:17px;color:var(--white)">They've said about us</h2>
  <p class="abs" style="left:130px;top:996px;width:370px;text-align:center;font-size:7px;line-height:9.5px;color:var(--white)">Lorem Ipsum is simply dummy text of the printing and typesetting industry. Lorem Ipsum has been the industry's standard dummy text ever since the 1500s, when an unknown printer took a galley of type Lorem Ipsum is simply dummy text of the printing and typesetting indus-</p>
  <div class="abs arrow" style="left:33px;top:1019px"></div>
  <div class="abs" style="left:47px;top:1026px;width:20px;height:1px;background:var(--white)"></div>
  <div class="abs" style="left:565px;top:1026px;width:20px;height:1px;background:var(--white)"></div>
  <div class="abs arrow" style="left:584px;top:1019px"></div>
  <div class="abs" role="img" aria-label="Portrait of the reviewer" style="left:230px;top:1035px;width:36px;height:36px;border-radius:50%;background:linear-gradient(#d9a56e,#8a5a3c);border:2px solid var(--white)"></div>
  <div class="abs display" style="left:272px;top:1033px;font-size:12px;color:var(--white)">Maren Holloway</div>
  <div class="abs script" style="left:287px;top:1050px;font-size:10px;color:var(--rose)">Business Owner Ltd</div>
  <div class="abs" style="left:292px;top:1062px;font-size:7px;color:#f5a623;letter-spacing:3px">★★★★★</div>

  <!-- faq -->
  <div class="abs script" style="left:70px;top:1150px;font-size:20px">Frequently asked questions</div>
  <div class="abs" style="left:70px;top:1175px;width:170px;height:1px;background:var(--rose)"></div>
  <h2 class="abs h2" style="left:64px;top:1185px;line-height:24px">We are working for the<br><span class="hl" style="margin-left:-3px">community</span></h2>
  <p class="abs body-text" style="left:63px;top:1253px;width:225px">Lorem Ipsum is simply dummy text of the printing and typesetting industry. Lorem Ipsum has been the industry's standard dummy text ever since the 1500s, when an unknown printer took a galley of type and scrambled it to make a type specimen book. It has survived not only five centuries, but also the leap into electronic typeset-</p>
  <svg class="abs" style="left:63px;top:1327px" width="22" height="22" viewBox="0 0 22 22"><circle cx="11" cy="11" r="11" fill="var(--rose)"/><path d="M7.5 6.5l2.2 2.3-1.2 1.4c.9 1.7 2 2.8 3.5 3.5l1.4-1.2 2.3 2.2-1.4 1.6c-3.8-.5-7.1-3.8-7.6-7.6z" fill="var(--white)"/></svg>
  <div class="abs" style="left:94px;top:1330px;font-size:13px;font-weight:600">123-456-789</div>

  <div class="abs acc" style="top:1148px;height:82px"><div class="q" style="border-bottom:1px solid var(--line)">What is cat sitting <span>^</span></div><p class="body-text" style="padding:6px 12px;font-weight:400">Lorem Ipsum is simply dummy text of the printing and typesetting industry. Lorem Ipsum has been the industry's standard dummy text ever since the 1500s, when an unknown printer took</p></div>
  <div class="abs acc" style="top:1246px"><div class="q">What is cat sitting <span>v</span></div></div>
  <div class="abs acc" style="top:1281px"><div class="q">What is cat sitting <span>v</span></div></div>
  <div class="abs acc" style="top:1316px"><div class="q">What is cat sitting <span>v</span></div></div>

  <!-- pricing -->
  <div class="abs script" style="left:0;top:1428px;width:630px;text-align:center;font-size:20px">Bring your pets</div>
  <div class="abs" style="left:258px;top:1452px;width:114px;height:1px;background:var(--rose)"></div>
  <h2 class="abs display" style="left:0;top:1464px;width:630px;text-align:center;font-size:17px;color:var(--ink)">The Best Choice</h2>

  <div class="abs card" style="left:102px;top:1513px"><div class="photo" role="img" aria-label="Photo of a long-haired cat resting" style="background:linear-gradient(135deg,#e9ddc8,#8a7560)"></div><div class="top"><span class="price">90$</span><span class="plan">Basic Plan</span></div><div class="per">Per Day</div><p>Lorem Ipsum is simply dummy text of the printing and typesetting industry. Lorem Ipsum has been the industry's standard dummy text ever since the 1500s,</p><ul><li><span class="tick"></span>Dui sapien eget mi.</li><li><span class="tick"></span>Dui sapien eget mi.</li><li><span class="tick"></span>Dui sapien eget mi.</li></ul></div>
  <div class="abs card" style="left:248px;top:1513px"><div class="photo" role="img" aria-label="Photo of a woman hugging a ginger cat" style="background:linear-gradient(135deg,#f3ede6,#d9a66c)"></div><div class="top"><span class="price">90$</span><span class="plan">Great Plan</span></div><div class="per">Per Day</div><p>Lorem Ipsum is simply dummy text of the printing and typesetting industry. Lorem Ipsum has been the industry's standard dummy text ever since the 1500s,</p><ul><li><span class="tick"></span>Dui sapien eget mi.</li><li><span class="tick"></span>Dui sapien eget mi.</li><li><span class="tick"></span>Dui sapien eget mi.</li></ul></div>
  <div class="abs card" style="left:393px;top:1513px"><div class="photo" role="img" aria-label="Photo of a cat beside a feeding bowl" style="background:linear-gradient(135deg,#b8a894,#6f6a66)"></div><div class="top"><span class="price">90$</span><span class="plan">Big Plan</span></div><div class="per">Per Day</div><p>Lorem Ipsum is simply dummy text of the printing and typesetting industry. Lorem Ipsum has been the industry's standard dummy text ever since the 1500s,</p><ul><li><span class="tick"></span>Dui sapien eget mi.</li><li><span class="tick"></span>Dui sapien eget mi.</li><li><span class="tick"></span>Dui sapien eget mi.</li></ul></div>

  <!-- footer -->
  <svg class="abs" style="left:0;top:1795px" width="630" height="395" viewBox="0 0 630 395">
    <path d="M0 5C30 45 80 73 160 77C260 81 330 85 400 135C460 180 540 205 630 222V395H0Z" fill="var(--rose)"/>
  </svg>
  <div class="abs partner" style="left:100px;top:1833px"></div>
  <div class="abs partner" style="left:175px;top:1833px"></div>
  <div class="abs partner" style="left:250px;top:1833px"></div>
  <div class="abs partner" style="left:325px;top:1833px"></div>
  <div class="abs partner" style="left:400px;top:1833px"></div>
  <div class="abs partner" style="left:475px;top:1833px"></div>

  <h2 class="abs display" style="left:0;top:1950px;width:600px;text-align:center;font-size:18px;color:var(--white)">Get New Insight Weekly</h2>
  <p class="abs" style="left:180px;top:1976px;width:240px;text-align:center;font-size:7px;line-height:9.5px;color:var(--white)">Lorem Ipsum is simply dummy text of the printing and typesetting industry. Lorem Ipsum has been the indus-</p>
  <div class="abs field" style="left:142px;top:2014px;width:138px">NAME</div>
  <div class="abs field" style="left:292px;top:2014px;width:176px">EMAIL</div>
  <span class="btn btn-green" style="left:405px;top:2014px;width:63px;height:22px;border-radius:11px">SUBSCRIBE</span>

  <div class="abs" style="left:142px;top:2058px;width:50px;height:55px;background:var(--white);border-radius:4px 4px 25px 25px;text-align:center;padding-top:8px"><div style="width:18px;height:18px;border-radius:50%;border:1.5px solid var(--green);margin:0 auto 2px"></div><div style="font-size:5px;font-weight:500;color:var(--rose);line-height:6px">Velvet Paws<br>Cat Sitting</div></div>
  <p class="abs" style="left:140px;top:2122px;width:90px;font-size:6.5px;line-height:8px;color:var(--white)">Lorem Ipsum is simply dummy text of the printing and typesetting industry.</p>
  <div class="abs" style="left:142px;top:2153px;display:flex;gap:3px"><i class="dot"></i><i class="dot"></i><i class="dot"></i><i class="dot"></i><i class="dot"></i><i class="dot"></i></div>

  <div class="abs foot" style="left:276px;top:2058px"><h4>Quick Links</h4><ul><li>Home</li><li>About</li><li>Services</li><li>Pricings</li><li>FAQs</li><li>Blogs</li></ul></div>
  <div class="abs foot" style="left:355px;top:2058px"><h4>Contact Me</h4><ul><li>☎ 123-456-789</li><li>⌂ Your Address Here</li><li>✉ Your Email Here</li><li>◎ Your Web Here</li></ul></div>
  <div class="abs foot" style="left:452px;top:2058px;width:100px"><h4>Working Hours</h4><p style="font-size:5.5px;line-height:7px;color:var(--white);margin-bottom:10px">Our support available to help you 24 hours a day. We provide our best</p><ul><li>Mon - Fri : 08.00 am - 20.00 pm</li><li>Saturday : 09.00 am - 20.00 pm</li><li>Sunday : We Are Closed</li></ul></div>

  <div class="abs copyright">copyright: all right reserved to velvetpawscatsitting.com, 2022</div>
</div>
</body>
</html>
```